Website for Scientific & Engineering Organization

Overview

The objective is to design a professional, easy-to-navigate, and visually appealing website for the <Enclosed Organization (see attached files)>, reflecting their esteemed status in the engineering and scientific community.

Pages:

Home (About Us) : Introduce the organization, highlighting their activities, history, and fellowship. Include a section for latest news highlights.

News and Programme : Dedicated page for news updates and detailed annual programmes

Gallery : This page will feature photographs and descriptions of the society's 'Voyages' and events.

Downloads : A section offering downloadable content such as newsletters and lecture materials, organized for user-friendliness.

Members Section : A private area for members to access exclusive content. Alternatively, a 'Membership' page with joining details and benefits if more public-facing content is preferred.

Design Elements:

Layout : A linear layout with a fixed top navigation bar for easy movement between pages.
Color Scheme : Utilize the provided colors (#395394, #E00053, #0043E1) to create a cohesive and professional aesthetic.
Typography : Use a combination of serif for headings and sans-serif for body text, ensuring readability and elegance.

Features:

Responsive Design : The design will accommodate various devices, ensuring consistency across mobiles, tablets, and desktops.

Accessibility : Design for all users with adequate spacing around elements and color contrasts

Content Strategy (Visual Focus):

Home Page : Visual emphasis on the introduction, mission, and recent 'Voyages' with engaging imagery and concise text.
News and Programme : Clear, visually distinct sections for news and the annual schedule
Gallery : A visually rich page with a grid or album layout, allowing users to easily browse through the years and events.
Downloads : Neatly organized sections with clear labels and icons to represent the different types of available downloads. Downloads are PDF newsletter/flyers/programmes etc...
Members Section/Membership : A design that conveys exclusivity and value, encouraging sign-ups and engagement from members.
Design Considerations:

Consistency : Ensure the design reflects the organization's heritage and professionalism throughout all pages.
User Experience : Focus on intuitive navigation and information architecture to guide visitors smoothly through the site.
Visual Hierarchy : Use size, color, and layout to emphasize key areas and direct user attention effectively.
Final Notes:

This design spec focuses on creating a web presence that mirrors the organization's prestige and heritage, providing an engaging, informative platform for members and the public alike. The design will be crafted to allow for easy content updates and adaptability, ensuring a long-lasting and effective website.

Target Market(s)

Non profit science and engineering. Older people

Industry/Entity Type

Non profit scientific organization

Number of Pages Required

5+ page

Requirements
Should not have
• No search feature

```html
<!DOCTYPE html>
<html lang="en">
<head>
<meta charset="utf-8">
<title>British Section of the CIFS</title>
<link rel="stylesheet" href="https://fonts.googleapis.com/css2?family=Libre+Baskerville:wght@400;700&family=Poppins:wght@400;500;600&display=swap">
<style>
:root{
  --navy:#395394;
  --pink:#e00053;
  --blue:#0043e1;
  --ink:#1d1d1f;
  --text:#3c3c44;
  --grey:#f1f1f3;
  --white:#ffffff;
  --black:#0c0c0e;
  --serif:'Libre Baskerville', Georgia, serif;
  --sans:'Poppins', Arial, sans-serif;
}
*{margin:0;padding:0;box-sizing:border-box}
html,body{width:1200px;height:4552px;overflow:hidden}
body{position:relative;background:var(--white);font-family:var(--sans);color:var(--text)}
.abs{position:absolute}
h1,h2,h3{font-family:var(--serif);color:var(--ink);font-weight:700}
.btn{display:inline-block;background:var(--pink);color:var(--white);font:500 15px var(--sans);padding:13px 22px;border-radius:4px;text-decoration:none}
.btn-outline{background:var(--white);color:var(--pink);border:2px solid var(--pink)}
.photo{position:absolute}

/* nav */
.site-nav{top:0;left:0;width:1200px;height:108px;background:var(--white);box-shadow:0 2px 8px rgba(0,0,0,.06)}
.brand{left:64px;top:28px;display:flex;align-items:center;gap:12px}
.brand-dot{width:40px;height:40px;border-radius:50%;background:var(--pink)}
.brand-name{font:600 30px var(--sans);color:var(--navy);letter-spacing:1px}
.nav-links{left:398px;top:44px;display:flex;gap:38px;list-style:none;font:400 15px var(--sans);color:var(--ink)}

/* hero */
.hero{top:108px;left:0;width:1200px;height:600px;background:linear-gradient(90deg,#35498a 0%,#52679f 45%,#8d98b4 70%,#b7b2aa 100%)}
.hero h1{left:112px;top:70px;width:540px;color:var(--white);font-size:37px;line-height:1.45}
.hero .btn{left:112px;top:406px}

.feature{top:596px;height:230px;background:var(--white);border-radius:8px;box-shadow:0 6px 24px rgba(0,0,0,.12);padding:26px 24px;text-align:center;font-size:13px;line-height:1.65}
.feature svg{display:block;margin:0 auto 14px}
.feature-alt{background:var(--pink);color:var(--white);display:flex;flex-direction:column;align-items:center;justify-content:center;gap:24px;font-size:15px}

/* who */
.who-img{left:140px;top:900px;width:340px;height:380px}
.who h2{left:604px;top:966px;font-size:36px}
.who p{left:604px;top:1026px;width:480px;font-size:14px;line-height:1.8}
.who .btn{left:604px;top:1140px}

/* activities */
.activities{top:1332px;left:0;width:1200px;height:660px;background:var(--grey)}
.activities h2{left:112px;top:74px;font-size:36px}
.activities p{left:112px;top:136px;width:460px;font-size:14px;line-height:1.9}
.activities .btn{left:112px;top:514px}
.activities .photo{left:644px;top:96px;width:400px;height:400px;background:linear-gradient(160deg,#d8b48a,#7a4c2b 60%,#3b2416)}

/* history */
.history-img{left:118px;top:2060px;width:330px;height:380px;background:linear-gradient(170deg,#a9a097,#6b5550 55%,#2f2a2c);border:8px solid var(--white);box-shadow:-10px -10px 0 #2f7d4f}
.history h2{left:636px;top:2124px;font-size:36px}
.history p{left:636px;top:2190px;width:470px;font-size:14px;line-height:1.8}
.history .btn{left:636px;top:2360px}

/* members */
.members{top:2564px;left:0;width:1200px;height:436px;background:linear-gradient(90deg,#2f4788,#3f5a9d 50%,#34508f)}
.members h2{left:0;top:90px;width:1200px;text-align:center;color:var(--white);font-size:36px}
.members p{left:230px;top:154px;width:740px;text-align:center;color:#e6e9f4;font-size:14px;line-height:1.9}
.members .btn{left:545px;top:290px}

/* news */
.news h2{left:0;top:3066px;width:1200px;text-align:center;font-size:36px}
.news-card{top:3160px;width:316px}
.news-card .photo{position:relative;height:250px;border-radius:4px}
.news-date{position:absolute;left:70px;top:228px;width:176px;height:40px;background:var(--pink);color:var(--white);font:500 14px/40px var(--sans);text-align:center;border-radius:4px}
.news-card h3{margin-top:40px;font-size:16px;line-height:1.45}
.news-card p{margin-top:8px;font-size:12px;line-height:1.6;text-transform:uppercase;height:60px}
.news-card .btn{margin-top:12px;padding:10px 18px;font-size:14px}
.slider-arrow{top:3268px;width:40px;height:40px;border-radius:50%;border:2px solid #9aa3bd;background:var(--white)}

/* closing band */
.closing{top:3640px;left:0;width:1200px;height:560px;background:var(--grey)}
.closing h2{left:112px;top:100px;width:500px;font-size:27px;line-height:1.45}
.closing p{left:112px;top:312px;width:440px;font-size:18px;line-height:1.6;color:var(--ink)}

/* footer */
.site-footer{top:4200px;left:0;width:1200px;height:352px;background:var(--black);color:#d8d8dc}
.site-footer .brand-dot{background:var(--white)}
.site-footer .brand-name{color:var(--white)}
.footer-col{top:74px}
.footer-col h4{font:600 18px var(--sans);color:var(--white);margin-bottom:16px}
.footer-col ul{list-style:none;font-size:14px;line-height:2.1}
.footer-col li::before{content:"›";color:var(--pink);margin-right:10px}
.contact-row{display:flex;gap:12px;font-size:14px;line-height:1.6;margin-bottom:14px;width:230px}
.footer-rule{left:0;top:290px;width:1200px;height:1px;background:#2c2c30}
.copyright{left:0;top:312px;width:1200px;text-align:center;font-size:14px;color:#c7c7cc}
</style>
</head>
<body>

<header class="abs site-nav">
  <div class="abs brand"><span class="brand-dot"></span><span class="brand-name">CIFS</span></div>
  <ul class="abs nav-links"><li>Home</li><li>Programme</li><li>Recent Meetings</li><li>History</li><li>Membership</li><li>Contact Us</li></ul>
</header>

<section class="abs hero">
  <div class="photo" style="left:560px;top:0;width:640px;height:600px;background:linear-gradient(120deg,rgba(255,255,255,0) 0%,rgba(210,205,195,.55) 60%,rgba(180,170,160,.6))" role="img" aria-label="Two engineers working together at a computer in a laboratory"></div>
  <h1 class="abs">Welcome to the British Section of the CIFS Sharing Knowledge and a Love of France</h1>
  <a class="abs btn">Get Started</a>
</section>

<div class="abs feature" style="left:208px;width:232px">
  <svg width="46" height="46" viewBox="0 0 46 46" fill="none" stroke="#e00053" stroke-width="2"><circle cx="23" cy="16" r="8"/><path d="M8 42c2-10 8-14 15-14s13 4 15 14"/></svg>
  An informal society of engineers and scientists, giving equal importance to the quality of our technical activities and our fellowship
</div>
<div class="abs feature" style="left:478px;width:242px">
  <svg width="46" height="46" viewBox="0 0 46 46" fill="none" stroke="#e00053" stroke-width="2"><circle cx="23" cy="23" r="18"/><circle cx="23" cy="23" r="10"/><circle cx="23" cy="23" r="3" fill="#e00053"/></svg>
  We provide high quality lectures and technical visits on diverse engineering and scientific subjects, and the enjoyment of French culture and cuisine
</div>
<div class="abs feature feature-alt" style="left:770px;width:232px">
  <span>New members are<br>always welcome</span>
  <a class="btn btn-outline" style="border:none">Learn More</a>
</div>

<section class="who">
  <svg class="abs who-img" viewBox="0 0 340 380" role="img" aria-label="Engineer in a hard hat on a site visit, in a hexagon frame">
    <defs><linearGradient id="whoFill" x1="0" y1="0" x2="1" y2="1"><stop offset="0" stop-color="#c9a25a"/><stop offset=".55" stop-color="#8a3a3a"/><stop offset="1" stop-color="#2d2f52"/></linearGradient></defs>
    <polygon points="170,6 332,98 332,282 170,374 8,282 8,98" fill="#395394"/>
    <polygon points="170,22 318,106 318,274 170,358 22,274 22,106" fill="url(#whoFill)"/>
  </svg>
  <h2 class="abs">Who We Are</h2>
  <p class="abs">We are an informal society of engineers and scientists. A very friendly organisation where equal importance is given to the quality of our technical activities and our fellowship, where our partners are involved and welcomed to everything we do.</p>
  <a class="abs btn">Learn More</a>
</section>

<section class="abs activities">
  <h2 class="abs">Our Activities</h2>
  <p class="abs">Five or six high quality technical lectures are arranged throughout the year at a number of London venues followed by dinner. Memorable lectures have included topics as diverse as the building of the Panama Canal, the origins of SI standard measurements and the current Antarctic research programme. There are normally two 'Voyages' each year of three or four days each, generally but not exclusively to France, where visits to technical or cultural establishments and major construction sites are undertaken. The 'Voyages' have equally important and enjoyable technical and social components, and of course, provide the opportunity and time to take in, enjoy and sample French culture and cuisine.</p>
  <a class="abs btn">Learn More</a>
  <div class="photo" role="img" aria-label="Members seated at a formal dinner in an ornate banqueting hall"></div>
</section>

<section class="history">
  <div class="abs history-img" role="img" aria-label="Group of society members posing together on a voyage"></div>
  <h2 class="abs">Our History</h2>
  <p class="abs">The British Section of the National Council of Allied Engineers and Scientists was founded on 27th June 1919 by members of the British Army returning from the war who wished to maintain links with their wartime colleagues in France.</p>
  <a class="abs btn">Learn More</a>
</section>

<section class="abs members">
  <h2 class="abs">Our Members</h2>
  <p class="abs">The origins of the Section lie in civil engineering. For many years, however, in line with the now named Société Franco-Scientifique des Ingénieurs (SFSI), we have been open to membership from like-minded people from all fields of engineering and science. We are always delighted to welcome new members.</p>
  <a class="abs btn">Learn More</a>
</section>

<section class="news">
  <h2 class="abs">Latest News</h2>
  <span class="abs slider-arrow" style="left:60px"><svg width="36" height="36" viewBox="0 0 36 36"><path d="M21 11l-7 7 7 7" fill="none" stroke="#395394" stroke-width="2"/></svg></span>
  <span class="abs slider-arrow" style="left:1100px"><svg width="36" height="36" viewBox="0 0 36 36"><path d="M15 11l7 7-7 7" fill="none" stroke="#395394" stroke-width="2"/></svg></span>

  <article class="abs news-card" style="left:110px">
    <div class="photo" style="background:linear-gradient(160deg,#8a8a7a,#4d4a3e 60%,#2a2824)" role="img" aria-label="Investigator examining burnt ground after a wildfire"><span class="news-date">09 January 2024</span></div>
    <h3>Incoming President's Inaugural lecture and dinner</h3>
    <p>Unexpected fire investigation: the underpinning fire science and investigative methods</p>
    <a class="btn btn-outline">Learn More</a>
  </article>
  <article class="abs news-card" style="left:442px">
    <div class="photo" style="background:linear-gradient(170deg,#3a2016,#c8501c 55%,#f3a23a)" role="img" aria-label="Wildfire burning through forest at night"><span class="news-date">19 March 2024</span></div>
    <h3>Evening Lecture and Dinner</h3>
    <p>How to protect people and homes from wildfires: nanoengineering and computer models</p>
    <a class="btn btn-outline">Learn More</a>
  </article>
  <article class="abs news-card" style="left:774px">
    <div class="photo" style="background:linear-gradient(180deg,#7f9cc4,#6d6f7c 50%,#d0642a 80%,#3a2a22)" role="img" aria-label="Tower block on fire against an evening sky"><span class="news-date">30 April 2024</span></div>
    <h3>Evening Lecture and Dinner</h3>
    <p>Unplanned adventures in fire science, engineering and regulation</p>
    <a class="btn btn-outline">Learn More</a>
  </article>
</section>

<section class="abs closing">
  <h2 class="abs">The Society for Engineers and Scientists where they sample French cuisine and culture with their partners as well as continue their professional interests</h2>
  <p class="abs">An Anglo-French Connection with Engineering and Science</p>
  <div class="photo" style="left:700px;top:90px;width:180px;height:170px;background:linear-gradient(160deg,#c9a26a,#7a4a2a)" role="img" aria-label="Dinner guests in a decorated hall"></div>
  <div class="photo" style="left:908px;top:150px;width:180px;height:170px;background:linear-gradient(160deg,#b4b7be,#5a5e6d)" role="img" aria-label="Members touring a historic street"></div>
  <div class="photo" style="left:700px;top:290px;width:180px;height:180px;background:linear-gradient(160deg,#b0855e,#3e2e30)" role="img" aria-label="Group of members in front of a monument"></div>
</section>

<footer class="abs site-footer">
  <div class="abs brand" style="left:112px;top:124px"><span class="brand-dot"></span><span class="brand-name">CIFS</span></div>
  <div class="abs footer-col" style="left:430px">
    <h4>Quick Links</h4>
    <ul><li>About Us</li><li>News &amp; Programme</li><li>Gallery</li><li>Downloads</li><li>Contact Us</li></ul>
  </div>
  <div class="abs footer-col" style="left:640px">
    <h4>Our Company</h4>
    <ul><li>Terms &amp; Conditions</li><li>Privacy Policy</li><li>About Us</li><li>Support</li></ul>
  </div>
  <div class="abs footer-col" style="left:862px">
    <h4>Contact us</h4>
    <div class="contact-row"><svg width="18" height="20" viewBox="0 0 18 22"><path d="M9 1a7 7 0 0 0-7 7c0 5 7 13 7 13s7-8 7-13a7 7 0 0 0-7-7z" fill="#e00053"/><circle cx="9" cy="8" r="2.5" fill="#0c0c0e"/></svg><span>Lorem ipsum dolor sit amet, consectetur adipiscing</span></div>
    <div class="contact-row"><svg width="18" height="18" viewBox="0 0 20 20"><path d="M4 2l3 0 2 5-2 1a10 10 0 0 0 5 5l1-2 5 2v3a2 2 0 0 1-2 2A16 16 0 0 1 2 4a2 2 0 0 1 2-2z" fill="#e00053"/></svg><span>+44 (0)20 7946 0158</span></div>
    <div class="contact-row"><svg width="18" height="16" viewBox="0 0 20 16"><rect x="1" y="1" width="18" height="14" rx="2" fill="#e00053"/><path d="M2 3l8 6 8-6" fill="none" stroke="#0c0c0e" stroke-width="1.5"/></svg><span>info@cifsnetwork.org</span></div>
  </div>
  <div class="abs footer-rule"></div>
  <div class="abs copyright">©Copyrights 2024 CIFS &nbsp;|&nbsp; All Rights Reserved</div>
</footer>

</body>
</html>
```